Quellmont Arbor Crew LLC company flyer

I need a flyer with information and photos about the tree trimming and removal services I provide. I want it to be elegant and organic. Include photos of my work that capture the essence, complexity and professionalism of my work. I want it to include information about the services we provide and information on why it is important to contract a certified arborist to manage your trees. I need it to be in Spanish as it is for Puerto Rico. Services we provide: especialistas en podas y remociones controladas de árboles y palmas, evaluaciones de riesgo de árboles, limpieza de palmas, transplante y siembra de árboles y palmas, arboristas certificados por la Liga Global de Silvicultura Vecinal (LGV). Contamos con Seguro de Responsabilidad Pública y CPT.

Target Market(s)

Homeowners, company owners, roo stay owners, hotels, restaurants,

Industry/Entity Type

Arboriculture

Requirements
Must have
• My LGV Certified Arborist logo

```html
<!DOCTYPE html>
<html lang="es">
<head>
<meta charset="utf-8">
<title>Quellmont Arbor Crew — Tree Service</title>
<link rel="stylesheet" href="https://fonts.googleapis.com/css2?family=Anton&family=Archivo+Black&family=Prompt:wght@400;500;600&display=swap">
<style>
  :root {
    --stage: #8c8c8c;
    --paper: #ffffff;
    --forest: #25281a;
    --olive: #87a03a;
    --olive-soft: #9bb14b;
    --ink: #1d1f16;
    --white: #ffffff;
    --mist: #e4e5e6;
  }
  * { margin: 0; padding: 0; box-sizing: border-box; }
  html, body {
    width: 1100px; height: 1200px; overflow: hidden;
    background: var(--stage);
  }
  .flyer {
    position: absolute; left: 72px; top: 0;
    width: 955px; height: 1200px;
    background: var(--paper);
    overflow: hidden;
    font-family: "Prompt", sans-serif;
  }
  .flyer-shapes { position: absolute; inset: 0; width: 955px; height: 1200px; }

  .brand { position: absolute; left: 0; top: 0; width: 450px; }
  .brand-mark {
    position: absolute; left: 158px; top: 54px;
    width: 130px; height: 130px; border-radius: 50%;
    border: 3px solid var(--forest);
  }
  .brand-name {
    position: absolute; left: 0; width: 450px; top: 199px;
    text-align: center; font-size: 18px; font-weight: 500;
    letter-spacing: 3px; color: var(--ink); text-transform: uppercase;
  }
  .brand-tagline {
    position: absolute; left: 0; width: 450px; top: 228px;
    text-align: center; font-size: 9px; font-weight: 500;
    letter-spacing: 4px; color: var(--olive); text-transform: uppercase;
  }

  .headline {
    position: absolute; left: 84px; top: 342px;
    font-family: "Anton", sans-serif; font-weight: 400; color: var(--white);
    font-size: 180px; line-height: 173px; letter-spacing: 3px;
    text-transform: uppercase; white-space: nowrap;
  }
  .headline-line { display: block; }

  .services-title {
    position: absolute; left: 90px; top: 703px;
    font-family: "Archivo Black", sans-serif; font-weight: 400; color: var(--olive);
    font-size: 40px; line-height: 43px; text-transform: uppercase;
  }
  .service-list { list-style: none; }
  .service-item {
    position: absolute; color: var(--white);
    font-size: 17px; line-height: 20px; padding-left: 36px;
  }
  .service-item svg { position: absolute; left: 0; top: 4px; width: 22px; height: 18px; }
  .service-item.a { left: 94px; top: 814px; width: 300px; }
  .service-item.b { left: 407px; top: 814px; width: 240px; }
  .service-item.c { left: 94px; top: 894px; width: 300px; }
  .service-item.d { left: 405px; top: 894px; width: 260px; }

  .contact { position: absolute; left: 96px; top: 954px; color: var(--white); font-weight: 600; font-style: normal; }
  .contact-phone { display: block; font-size: 25px; line-height: 32px; }
  .contact-email { display: block; font-size: 27px; line-height: 34px; }

  .credential-badge {
    position: absolute; left: 82px; top: 1051px;
    width: 52px; height: 80px; background: var(--olive);
    border: 3px solid var(--white);
  }
  .insured-seal {
    position: absolute; left: 150px; top: 1044px;
    width: 92px; height: 92px; border-radius: 50%;
    background: var(--olive); opacity: .85;
  }
  .certification {
    position: absolute; left: 254px; top: 1066px;
    color: var(--white); font-size: 17px; line-height: 24px;
  }

  .footer-bar {
    position: absolute; left: 0; top: 1148px; width: 955px; height: 33px;
    background: var(--olive); color: var(--ink);
    text-align: center; font-size: 18px; line-height: 33px;
  }
</style>
</head>
<body>
<main class="flyer">
  <svg class="flyer-shapes" viewBox="0 0 1158 1455" preserveAspectRatio="none">
    <defs>
      <linearGradient id="canopyTone" x1="0" y1="0" x2="1" y2="1">
        <stop offset="0" stop-color="#3f6a2a"/>
        <stop offset=".45" stop-color="#6f8f4a"/>
        <stop offset=".7" stop-color="#8fb3d6"/>
        <stop offset="1" stop-color="#5a4a36"/>
      </linearGradient>
      <radialGradient id="stumpTone" cx=".55" cy=".5" r=".6">
        <stop offset="0" stop-color="#d99a88"/>
        <stop offset=".45" stop-color="#7c6b52"/>
        <stop offset="1" stop-color="#4d6e34"/>
      </radialGradient>
      <linearGradient id="climberTone" x1="0" y1="0" x2="0" y2="1">
        <stop offset="0" stop-color="#c4492f"/>
        <stop offset=".45" stop-color="#9a7a62"/>
        <stop offset="1" stop-color="#e9642b"/>
      </linearGradient>
      <radialGradient id="dotHaze" cx=".3" cy=".3" r=".7">
        <stop offset="0" stop-color="#e2e3e4"/>
        <stop offset="1" stop-color="#ffffff" stop-opacity="0"/>
      </radialGradient>
      <clipPath id="stumpClip"><circle cx="972" cy="489" r="195"/></clipPath>
    </defs>

    <rect class="haze" x="0" y="0" width="460" height="340" fill="url(#dotHaze)" role="img" aria-label="Soft grey halftone texture"/>
    <rect class="haze" x="940" y="620" width="218" height="420" fill="url(#dotHaze)" role="img" aria-label="Soft grey halftone texture"/>

    <path class="canopy-photo" d="M600,0 C620,200 700,340 800,445 L1158,445 L1158,0 Z" fill="url(#canopyTone)" role="img" aria-label="Photo of an arborist in an orange helmet climbing and cutting a large tree"/>
    <path d="M576,0 C596,210 680,352 792,460" fill="none" stroke="var(--olive)" stroke-width="22"/>

    <path class="forest-field" d="M0,345 C300,305 620,360 810,478 L972,694 C1040,780 1090,870 1158,990 L1158,1455 L0,1455 Z" fill="var(--forest)"/>
    <path d="M0,345 C300,305 620,360 810,478" fill="none" stroke="var(--olive)" stroke-width="22"/>
    <path d="M972,694 C1040,780 1090,870 1158,990" fill="none" stroke="var(--olive)" stroke-width="5"/>

    <circle cx="972" cy="489" r="199" fill="var(--white)"/>
    <rect x="777" y="294" width="390" height="390" clip-path="url(#stumpClip)" fill="url(#stumpTone)" role="img" aria-label="Close-up photo of a freshly cut tree limb"/>

    <path class="climber-photo" d="M790,1390 L830,1250 L900,1150 L920,900 L1000,852 L1100,870 L1158,930 L1158,1390 Z" fill="url(#climberTone)" role="img" aria-label="Portrait photo of the certified arborist in helmet and orange safety shirt"/>

    <rect x="0" y="1432" width="1158" height="23" fill="var(--forest)"/>
  </svg>

  <header class="brand">
    <span class="brand-mark"></span>
    <p class="brand-name">Quellmont Arbor Crew</p>
    <p class="brand-tagline">Manejo de árboles</p>
  </header>

  <h1 class="headline"><span class="headline-line">Tree</span><span class="headline-line">Service</span></h1>

  <h2 class="services-title">Services<br>we provide</h2>
  <ul class="service-list">
    <li class="service-item a"><svg viewBox="0 0 22 18"><polyline points="2,9 8,15 20,2" fill="none" stroke="#87a03a" stroke-width="3"/></svg>especialistas en podas y remociones controladas de árboles y palmas,</li>
    <li class="service-item b"><svg viewBox="0 0 22 18"><polyline points="2,9 8,15 20,2" fill="none" stroke="#87a03a" stroke-width="3"/></svg>limpieza de<br>palmas</li>
    <li class="service-item c"><svg viewBox="0 0 22 18"><polyline points="2,9 8,15 20,2" fill="none" stroke="#87a03a" stroke-width="3"/></svg>evaluaciones de riesgo<br>de árboles</li>
    <li class="service-item d"><svg viewBox="0 0 22 18"><polyline points="2,9 8,15 20,2" fill="none" stroke="#87a03a" stroke-width="3"/></svg>transplante y siembra<br>de árboles y palmas</li>
  </ul>

  <address class="contact">
    <span class="contact-phone">+1 787-555-0142</span>
    <span class="contact-email">contacto@quellmontarbor.com</span>
  </address>

  <span class="credential-badge"></span>
  <span class="insured-seal"></span>
  <p class="certification">arboristas certificados por la Liga Global<br>de Silvicultura Vecinal (LGV)</p>

  <footer class="footer-bar">Contamos con Seguro de Responsabilidad Pública y CPT.</footer>
</main>
</body>
</html>
```